Brazilian food stall looking for a make over

We need a new Design for the front of our stall that would look authentic, colourful and practical as we have to transport, set up and put down in few hours.
We are based in Brisbane and our business are call The Ember Coals.
We sell Brazilian traditional BBQ and vegetarians options at markets, festivals and privet functions. We are new to this business and at the moment we are using our own design as presented on the image below.
We would like to see designs that would be eye catching with high contrast for easy recognition of the product with a menu with images of the product.

Requirements
Must have
• A connection with the product that is Brazilian bbq

```html
<!DOCTYPE html>
<html lang="en">
<head>
<meta charset="utf-8">
<title>The Brazilian BBQ Feast – Stall Graphics</title>
<link rel="stylesheet" href="https://fonts.googleapis.com/css2?family=Lobster&family=Roboto+Condensed:wght@400;700&display=swap">
<style>
  :root {
    --page: #ecebe8;
    --brown-deep: #3e120a;
    --brown-mid: #6e2410;
    --brown-glow: #9a3d18;
    --cream: #fff6e6;
    --gold: #f7c21c;
    --flame-red: #d8260d;
    --flame-orange: #f27a12;
    --plate-white: #f4efe6;
    --herb-green: #5d8a2c;
    --char: #2a1208;
  }
  * { box-sizing: border-box; margin: 0; padding: 0; }
  html, body { width: 1149px; height: 1200px; overflow: hidden; }
  body {
    background: var(--page);
    font-family: "Roboto Condensed", Arial, sans-serif;
    position: relative;
  }
  .panel {
    position: absolute;
    background: radial-gradient(ellipse at 50% 45%, var(--brown-glow) 0%, var(--brown-mid) 45%, var(--brown-deep) 100%);
    color: var(--cream);
    overflow: hidden;
    box-shadow: 0 2px 8px rgba(0,0,0,.25);
  }
  .feast-title {
    font-family: "Lobster", cursive;
    font-weight: 400;
    color: var(--cream);
    text-align: center;
    line-height: 1;
    white-space: nowrap;
  }
  .feast-title .the { font-size: .55em; vertical-align: .35em; margin-right: .1em; }
  .brand-name {
    font-family: "Roboto Condensed", Arial, sans-serif;
    font-weight: 700;
    color: var(--gold);
    text-transform: uppercase;
    letter-spacing: .03em;
    text-align: center;
    line-height: 1.05;
    white-space: nowrap;
  }
  .photo {
    position: absolute;
    border-radius: 50%;
    border: 4px solid var(--flame-orange);
    box-shadow: 0 0 14px rgba(0,0,0,.45);
  }
  .photo.skewer-hearts { background: radial-gradient(circle at 45% 40%, #e8a45c 0%, #a4521f 40%, #5a2a12 75%, #2e150a 100%); }
  .photo.steak-roll    { background: radial-gradient(ellipse at 50% 55%, #7fa640 0%, #d9b27a 30%, #9a5a2a 60%, #4a2410 100%); }
  .photo.fire-beef     { background: radial-gradient(circle at 50% 30%, #ffd04a 0%, #f27a12 30%, #8a3a18 60%, var(--char) 100%); }
  .photo.rice-plate    { background: radial-gradient(circle at 50% 55%, #f6d86a 0%, var(--plate-white) 35%, #d8482a 65%, #8a2318 100%); }
  .flame-halo {
    position: absolute;
    width: 110px; height: 70px;
    border-radius: 50% 50% 40% 40%;
    background: radial-gradient(ellipse at 50% 80%, var(--gold) 0%, var(--flame-orange) 45%, rgba(216,38,13,0) 75%);
  }
  .price-badge {
    position: absolute;
    border-radius: 50%;
    background: radial-gradient(circle at 40% 35%, var(--gold), var(--flame-orange));
    color: var(--flame-red);
    font-weight: 700;
    display: flex; align-items: center; justify-content: center;
    white-space: nowrap;
  }
  .menu-copy { text-align: center; line-height: 1.3; }
  .menu-copy .choice { color: var(--gold); font-weight: 700; }

  /* header banner */
  .header-banner { left: 40px; top: 40px; width: 1069px; height: 230px; }
  .header-banner .hero-food {
    position: absolute; left: 40px; top: 20px; width: 220px; height: 195px;
    border-radius: 24px;
    background:
      radial-gradient(ellipse at 45% 40%, #ffd04a 0%, #f27a12 25%, rgba(242,122,18,0) 55%),
      radial-gradient(ellipse at 70% 80%, #b8864a 0%, #7a3e1a 35%, rgba(110,36,16,0) 70%),
      radial-gradient(ellipse at 20% 80%, #e8b04a 0%, #a0521c 35%, rgba(110,36,16,0) 65%);
  }
  .header-banner .feast-title { position: absolute; left: 260px; width: 600px; top: 36px; font-size: 84px; }
  .header-banner .brand-name { position: absolute; right: 40px; bottom: 38px; font-size: 26px; }

  /* side banner */
  .side-banner { left: 40px; top: 300px; width: 260px; height: 860px; }
  .side-banner .brand-name { margin-top: 42px; font-size: 26px; }
  .side-banner .feast-title { margin-top: 50px; font-size: 46px; line-height: 1.1; }
  .side-banner .menu-copy { margin-top: 40px; font-size: 17px; padding: 0 14px; }
  .side-banner .photo { left: 25px; top: 530px; width: 180px; height: 180px; border-color: var(--cream); }
  .side-banner .price-badge { left: 168px; top: 650px; width: 80px; height: 80px; font-size: 26px; }
  .side-banner .flames {
    position: absolute; left: 0; bottom: 0; width: 260px; height: 110px;
    background: linear-gradient(to top, var(--flame-red) 0%, var(--flame-orange) 45%, rgba(247,194,28,0) 100%);
  }

  /* counter banner */
  .counter-banner { left: 330px; top: 300px; width: 779px; height: 430px; }
  .counter-banner .feast-title { margin-top: 30px; font-size: 64px; }
  .counter-banner .photo-row { position: absolute; left: 0; right: 0; top: 190px; height: 220px; }
  .counter-banner .photo { width: 165px; height: 165px; top: 35px; }
  .counter-banner .flame-halo { top: 0; }
  .counter-banner .slot-1 { left: 30px; }
  .counter-banner .slot-2 { left: 218px; }
  .counter-banner .slot-3 { left: 406px; }
  .counter-banner .slot-4 { left: 594px; }
  .counter-banner .flame-halo.slot-1 { left: 57px; }
  .counter-banner .flame-halo.slot-2 { left: 245px; }
  .counter-banner .flame-halo.slot-3 { left: 433px; }
  .counter-banner .flame-halo.slot-4 { left: 621px; }

  /* menu sign */
  .menu-sign { left: 580px; top: 760px; width: 300px; height: 400px; }
  .menu-sign .brand-name { margin-top: 20px; font-size: 22px; }
  .menu-sign .feast-title { margin-top: 14px; font-size: 26px; }
  .menu-sign .menu-copy { margin-top: 16px; font-size: 14px; padding: 0 20px; }
  .menu-sign .photo { left: 40px; top: 235px; width: 130px; height: 130px; border-color: var(--cream); }
  .menu-sign .price-badge { left: 165px; top: 285px; width: 60px; height: 60px; font-size: 19px; }
  .menu-sign .corner-glow {
    position: absolute; right: 0; bottom: 0; width: 110px; height: 90px;
    background: radial-gradient(ellipse at 100% 100%, var(--flame-orange) 0%, rgba(216,38,13,.6) 40%, rgba(110,36,16,0) 75%);
  }
</style>
</head>
<body>

<section class="panel header-banner">
  <div class="hero-food" role="img" aria-label="Skewered meats over flames with grilled chicken and a steak roll"></div>
  <h1 class="feast-title"><span class="the">The</span>Brazilian BBQ<br>Feast</h1>
  <div class="brand-name">The Ember Coals</div>
</section>

<section class="panel side-banner">
  <div class="brand-name">The Ember Coals</div>
  <h2 class="feast-title"><span class="the">The</span><br>Brazilian<br>BBQ Feast</h2>
  <p class="menu-copy">
    <span class="choice">Choice of Beef Or Chicken</span><br>
    Served with: Feijao preto<br>
    (Black bean casserole)<br>
    Arroz (Rice)<br>
    Vinaigrette Salad
  </p>
  <div class="photo fire-beef" role="img" aria-label="Grilled beef on a skewer over flames"></div>
  <div class="price-badge">$ 13</div>
  <div class="flames" role="img" aria-label="Rising flames"></div>
</section>

<section class="panel counter-banner">
  <h2 class="feast-title"><span class="the">The</span>Brazilian BBQ<br>Feast</h2>
  <div class="photo-row">
    <div class="flame-halo slot-1" role="img" aria-label="Flame"></div>
    <div class="flame-halo slot-2" role="img" aria-label="Flame"></div>
    <div class="flame-halo slot-3" role="img" aria-label="Flame"></div>
    <div class="flame-halo slot-4" role="img" aria-label="Flame"></div>
    <div class="photo skewer-hearts slot-1" role="img" aria-label="Chicken hearts on a skewer"></div>
    <div class="photo steak-roll slot-2" role="img" aria-label="Steak roll with green sauce"></div>
    <div class="photo fire-beef slot-3" role="img" aria-label="Grilled beef over flames"></div>
    <div class="photo rice-plate slot-4" role="img" aria-label="Plate of rice, salad and beetroot"></div>
  </div>
</section>

<section class="panel menu-sign">
  <div class="brand-name">The Ember Coals</div>
  <h2 class="feast-title"><span class="the">The</span>Brazilian BBQ Feast</h2>
  <p class="menu-copy">
    <span class="choice">Choice of Beef Or Chicken</span><br>
    Served with: Feijao preto<br>
    (Black bean casserole) Arroz (Rice)<br>
    Vinaigrette Salad
  </p>
  <div class="photo fire-beef" role="img" aria-label="Grilled beef on a skewer"></div>
  <div class="price-badge">$ 13</div>
  <div class="corner-glow" role="img" aria-label="Flame"></div>
</section>

</body>
</html>
```